Consulting, Investors, Joint Venture Website

Founded in April 2018, Marendo Consultants Limited (MCL) is an advisory consulting firm specializing in engaging investors in business ventures in Tanzania.
With extensive experience in construction, energy, oil and gas and the legal professions, our team assembles our expertise that allows foreign investors to set foot and flourish in the Tanzanian market.
MCL is locally owned, founded and registered. Our shareholders are cultured Tanzanian citizens with extensive corporate experience in South Africa, Tanzania, United Kingdom and the United States.

Our mission is to provide responsive and unrivalled professional advice from learned and experienced professionals versed in the local market, with an understanding of the cultural and logistical challenges faced by foreign investors.

Our vision is to provide a complete investor’s package that initiates with company registration, compliance and documentation services and ultimately operational facilitation services.

Target Market(s)

Foreign Investors, International companies

Industry/Entity Type

Business Consultant

Number of Pages Required

5+ page

Requirements
Must have
• It will be 5 pages - Home, About Us, Services, Portfolio, Contact Us
Nice to have
• if it can look like https://www.plorvex.example/
• or https://www.dunetri.example or http://www.quillbrook.example/

```html
<!DOCTYPE html>
<html lang="en">
<head>
<meta charset="utf-8">
<title>Marendo Consultants</title>
<link rel="stylesheet" href="https://fonts.googleapis.com/css2?family=Oswald:wght@400;500&family=Jost:wght@400;500;600;700&family=Dancing+Script:wght@500&family=Raleway:wght@400;500&display=swap">
<style>
:root{
  --brand:#0e6a96;
  --brand-deep:#0a6790;
  --brand-bright:#0d7ba8;
  --ink:#222;
  --muted:#8a8a8a;
  --paper:#fdf9f9;
  --white:#fff;
  --footer:#4a4a4a;
  --footer-deep:#333;
}
*{margin:0;padding:0;box-sizing:border-box}
html,body{width:710px;height:1200px;overflow:hidden;background:var(--white)}
body{position:relative;font-family:'Jost',sans-serif;color:var(--ink)}
.abs{position:absolute}
.center{left:0;right:0;text-align:center}

/* hero */
.hero{top:0;left:0;width:710px;height:398px;background:linear-gradient(180deg,#bcd3e6 0%,#dfe8f0 45%,#eef1f4 70%,#c9d2da 100%)}
.brand{top:14px;left:60px;display:flex;align-items:center;gap:8px;font-family:'Oswald',sans-serif;font-size:18px;font-weight:500;color:#1d2b36}
.brand-dot{width:24px;height:24px;border-radius:50%;background:var(--brand)}
.nav{top:18px;left:444px;display:flex;font-family:'Oswald',sans-serif;font-size:12px;color:#6d7780}
.nav a{color:inherit;text-decoration:none;margin-right:26px}
.nav a.current{color:#1d2b36;border-bottom:1px solid var(--brand);padding-bottom:1px}
.hero-script{top:148px;font-family:'Dancing Script',cursive;font-size:40px;color:#2d2d2d;margin-left:30px}
.hero-title{top:176px;font-size:48px;font-weight:700;color:var(--brand);letter-spacing:1px}
.tab{background:var(--white);text-align:center}
.tab-hello{top:376px;left:308px;width:93px;height:22px;font-size:12px;line-height:22px;color:#333}

/* welcome */
.welcome{top:398px;left:0;width:710px;height:169px;background:var(--paper)}
.section-title{font-size:21px;font-weight:600;color:var(--ink)}
.section-sub{font-size:10px;color:#333}
.rule{height:2px;background:var(--brand)}
.pillar{width:130px;text-align:center}
.pillar h3{font-family:'Oswald',sans-serif;font-weight:400;font-size:15px;color:var(--ink);margin-bottom:6px}
.pillar p{width:116px;margin:0 auto;font-size:7.5px;line-height:10.5px;color:var(--muted)}

/* team */
.team{top:567px;left:0;width:710px;height:261px;background:linear-gradient(180deg,var(--brand-bright),var(--brand-deep))}
.team-title{top:19px;font-size:20px;font-weight:600;color:var(--white);letter-spacing:.5px}
.member{top:64px;width:130px;text-align:center;color:var(--white)}
.portrait{width:113px;height:113px;border-radius:50%;margin:0 auto 8px}
.member h4{font-family:'Oswald',sans-serif;font-weight:500;font-size:12px}
.member span{font-size:7.5px;display:block}
.tab-follow{top:803px;left:306px;width:98px;height:25px;font-size:12px;font-weight:600;line-height:25px;color:var(--brand)}

/* case studies */
.study{top:900px;width:120px;text-align:center}
.study-img{width:120px;height:120px;margin-bottom:10px}
.study h4{font-family:'Oswald',sans-serif;font-weight:400;font-size:12px;color:var(--ink)}
.study span{font-size:7.5px;color:#555;display:block}

/* footer */
.footer{top:1072px;left:0;width:710px;height:93px;background:var(--footer);color:var(--white)}
.footer-title{top:20px;font-size:21px;font-weight:600}
.footer-link{top:46px;font-size:8px;text-decoration:underline}
.footer-nav{top:71px;left:62px;width:586px;display:flex;justify-content:space-between;align-items:center;font-family:'Raleway',sans-serif;font-size:12px;white-space:nowrap}
.footer-nav i{font-style:normal;font-size:7px}
.bottom{top:1165px;left:0;width:710px;height:35px;background:var(--footer-deep);font-family:'Raleway',sans-serif;font-size:11px;color:#9a9a9a}
.copy{top:11px;left:59px}
.social{top:10px;left:489px;display:flex;align-items:center;gap:12px}
.social b{width:14px;height:14px;border-radius:50%;background:var(--white);display:block}
</style>
</head>
<body>

<header class="hero abs" role="img" aria-label="City skyline of towers rising above low clouds"></header>
<div class="brand abs"><span class="brand-dot"></span>Marendo Consultants</div>
<nav class="nav abs"><a class="current" href="#">Home</a><a href="#">About</a><a href="#">Services</a><a href="#">Contact</a></nav>
<div class="hero-script abs center">always</div>
<h1 class="hero-title abs center">DO THE RIGHT THING</h1>
<div class="tab tab-hello abs">Say Hello!</div>

<section class="welcome abs">
  <h2 class="section-title abs center" style="top:26px">Welcome to Marendo Consultants</h2>
  <div class="rule abs" style="top:58px;left:181px;width:73px"></div>
  <div class="rule abs" style="top:58px;left:455px;width:73px"></div>
  <p class="section-sub abs center" style="top:52px">Let’s make a game Changing Strategy</p>
  <div class="pillar abs" style="left:82px;top:90px"><h3>Idea</h3><p>Lorem Ipsum is simply dummy text of the printing and type setting industry.</p></div>
  <div class="pillar abs" style="left:290px;top:90px"><h3>Planning</h3><p>Lorem Ipsum is simply dummy text of the printing and type setting industry.</p></div>
  <div class="pillar abs" style="left:498px;top:90px"><h3>Success</h3><p>Lorem Ipsum is simply dummy text of the printing and type setting industry.</p></div>
</section>

<section class="team abs">
  <h2 class="team-title abs center">MEET OUR TEAM</h2>
  <div class="member abs" style="left:55px"><div class="portrait" role="img" aria-label="Portrait of the managing director" style="background:radial-gradient(circle,#b08b72,#6d7378)"></div><h4>Lorem Ipsum</h4><span>Managing Director</span></div>
  <div class="member abs" style="left:209px"><div class="portrait" role="img" aria-label="Portrait of the strategic head" style="background:radial-gradient(circle,#d9a98a,#7a6a50)"></div><h4>Lorem Ipsum</h4><span>Strategic Head</span></div>
  <div class="member abs" style="left:362px"><div class="portrait" role="img" aria-label="Portrait of the support provider" style="background:radial-gradient(circle,#6b4a3a,#8a7060)"></div><h4>Lorem Ipsum</h4><span>Support Peovider</span></div>
  <div class="member abs" style="left:524px"><div class="portrait" role="img" aria-label="Portrait of the technical lead" style="background:radial-gradient(circle,#c9a48c,#4a3a32)"></div><h4>Lorem Ipsum</h4><span>Technical Banda</span></div>
</section>
<div class="tab tab-follow abs">Follow us!</div>

<h2 class="section-title abs center" style="top:844px">Read Our Case Studies</h2>
<div class="rule abs" style="top:876px;left:216px;width:59px"></div>
<div class="rule abs" style="top:876px;left:435px;width:59px"></div>
<p class="section-sub abs center" style="top:870px">Well Researched Case Studies</p>
<div class="study abs" style="left:58px"><div class="study-img" role="img" aria-label="Hand writing figures in a notebook" style="background:linear-gradient(135deg,#6b4a2e,#d7dde0)"></div><h4>Lorem Ipsum</h4><span>Market Resurch #2</span></div>
<div class="study abs" style="left:214px"><div class="study-img" role="img" aria-label="Calculator on a handwritten business plan" style="background:linear-gradient(160deg,#555,#e8e8e4 55%)"></div><h4>Lorem Ipsum</h4><span>Market Growth</span></div>
<div class="study abs" style="left:367px"><div class="study-img" role="img" aria-label="Spreadsheet ledger printout" style="background:linear-gradient(135deg,#e9b9a0,#dcdfe6)"></div><h4>Lorem Ipsum</h4><span>Technology in Business</span></div>
<div class="study abs" style="left:529px"><div class="study-img" role="img" aria-label="Computer mouse on a financial newspaper" style="background:linear-gradient(135deg,#2e5c9a,#cfcfcf 60%)"></div><h4>Lorem Ipsum</h4><span>Right Timing</span></div>

<footer class="footer abs">
  <h2 class="footer-title abs center">Feel Free To Communicate</h2>
  <a class="footer-link abs center" style="color:var(--white)" href="#">Book an Appointment!</a>
  <nav class="footer-nav abs"><span>Home</span><i>●</i><span>About</span><i>●</i><span>Services</span><i>●</i><span>Case Studies</span><i>●</i><span>Our Team</span><i>●</i><span>Process</span><i>●</i><span>Contact</span></nav>
</footer>
<div class="bottom abs">
  <span class="copy abs">2020 copyright by the business group</span>
  <div class="social abs"><span>Follow us on</span><b></b><b></b><b></b></div>
</div>

</body>
</html>
```